Re-design of Business Card

We require a design for our business card.

Korrim is a supplier of industrial packaging specializing in plastic products. We are undergoing a rebranding to appear more corporate. We have changed our company name to korrim and have a new logo.

I have uploaded our old card design with the previous company name.
Don't copy the current design. We are looking for a new design.

Industry/Entity Type

Manufacturing

Contact Information for Business Card

please don't copy the current design. we are looking for a new design.

Font styles to use
Sans Serif

Colors

Designer to choose colors to be used in the design.

Requirements
Must have
• clean and easy to read.

```html
<!DOCTYPE html>
<html lang="en">
<head>
<meta charset="utf-8">
<title>Korrim Business Card</title>
<link href="https://fonts.googleapis.com/css2?family=Montserrat:wght@700;800&family=Mulish:wght@400&display=swap" rel="stylesheet">
<style>
  :root {
    --page: #ececec;
    --card: #2b2b2b;
    --orange: #d9711f;
    --orange-deep: #c7641b;
    --shadow: rgba(0,0,0,0.18);
  }
  * { box-sizing: border-box; margin: 0; padding: 0; }
  html, body { width: 1200px; height: 1200px; overflow: hidden; background: var(--page); }
  .card {
    position: absolute; left: 44px; width: 1120px; height: 504px;
    background: var(--card); color: var(--orange);
    box-shadow: 0 2px 6px var(--shadow);
    font-family: "Mulish", sans-serif;
  }
  .card-front { top: 38px; }
  .card-back { top: 634px; }

  .brand-name {
    position: absolute; display: flex; align-items: center; justify-content: center;
    font-family: "Montserrat", sans-serif; font-weight: 800;
    color: var(--orange); letter-spacing: 4px; line-height: 1; white-space: nowrap;
  }
  .card-front .brand-name { left: 55px; top: 203px; width: 418px; height: 96px; font-size: 80px; }
  .card-back .brand-name { left: 684px; top: 57px; width: 365px; height: 84px; font-size: 70px; }

  .divider { position: absolute; left: 511px; top: 68px; width: 13px; height: 346px; background: var(--orange); }

  .person-name {
    position: absolute; left: 556px; top: 60px; white-space: nowrap;
    font-family: "Montserrat", sans-serif; font-weight: 800; font-size: 45px; line-height: 1; letter-spacing: 0.5px;
  }
  .person-title {
    position: absolute; left: 564px; top: 104px; white-space: nowrap;
    font-size: 22px; line-height: 1; letter-spacing: 1.6px;
  }

  .contact-list { position: absolute; left: 554px; top: 0; list-style: none; }
  .contact-item { position: absolute; left: 0; display: flex; align-items: flex-start; white-space: nowrap; }
  .contact-item svg { width: 36px; height: 26px; flex: none; margin-right: 10px; margin-top: 1px; fill: var(--orange); }
  .contact-text { font-size: 25px; letter-spacing: 1.3px; line-height: 27px; }
  .item-phone { top: 179px; } .item-fax { top: 222px; } .item-mail { top: 266px; }
  .item-web { top: 316px; } .item-address { top: 365px; }

  .coverage-map {
    position: absolute; left: 55px; top: 37px; width: 460px; height: 242px;
    border-radius: 14px;
    background: linear-gradient(160deg, var(--orange) 0%, var(--orange-deep) 100%);
  }

  .badge-row { position: absolute; top: 163px; left: 740px; display: flex; gap: 25px; }
  .badge { width: 96px; height: 96px; border-radius: 50%; border: 6px solid var(--orange); }

  .range { position: absolute; top: 282px; }
  .range-heading {
    font-family: "Montserrat", sans-serif; font-weight: 700; font-size: 20px;
    letter-spacing: 0.9px; line-height: 24px; white-space: nowrap;
  }
  .range-list { list-style: none; margin-top: 30px; font-size: 19px; letter-spacing: 0.9px; line-height: 23.5px; }
  .range-list li { padding-left: 12px; text-indent: -12px; }
  .range-list li::before { content: ". "; }
  .range-pallet { left: 52px; }
  .range-flexible { left: 322px; }
  .range-flexible .range-list { margin-top: 36px; }
  .range-machinery { left: 592px; width: 240px; }
  .range-machinery .range-list { margin-top: 6px; width: 225px; }
  .range-general { left: 833px; }
</style>
</head>
<body>

<section class="card card-front">
  <div class="brand-name">KORRIM</div>
  <div class="divider"></div>
  <h1 class="person-name">Declan Marsh</h1>
  <p class="person-title">Machinery Sales Manager</p>
  <ul class="contact-list">
    <li class="contact-item item-phone">
      <svg viewBox="0 0 24 24"><path d="M6.6 10.8a15.1 15.1 0 0 0 6.6 6.6l2.2-2.2c.3-.3.7-.4 1-.2 1.1.4 2.3.6 3.6.6.6 0 1 .4 1 1V20c0 .6-.4 1-1 1A17 17 0 0 1 3 4c0-.6.4-1 1-1h3.5c.6 0 1 .4 1 1 0 1.3.2 2.5.6 3.6.1.3 0 .7-.2 1z"/></svg>
      <span class="contact-text">1300 415 806</span>
    </li>
    <li class="contact-item item-fax">
      <svg viewBox="0 0 24 24"><path d="M7 3h10v4H7zM3 8h18a1 1 0 0 1 1 1v7h-4v4H6v-4H2V9a1 1 0 0 1 1-1zm5 7v3h8v-3z"/></svg>
      <span class="contact-text">+61 738 204 517</span>
    </li>
    <li class="contact-item item-mail">
      <svg viewBox="0 0 24 24"><path d="M2 5h20v14H2zm2.5 2 7.5 5.5L19.5 7zM4 9v8h16V9l-8 6z"/></svg>
      <span class="contact-text">sales@tarrantpacking.com.au</span>
    </li>
    <li class="contact-item item-web">
      <svg viewBox="0 0 24 24"><path d="M12 2a10 10 0 1 0 0 20 10 10 0 0 0 0-20zm-1 2.1V8H7.6A8 8 0 0 1 11 4.1zm2 0A8 8 0 0 1 16.4 8H13zM5 10h6v4H5zm8 0h6v4h-6zm-5.4 6H11v3.9A8 8 0 0 1 7.6 16zm5.4 0h3.4a8 8 0 0 1-3.4 3.9z"/></svg>
      <span class="contact-text">www.korrim.com.au</span>
    </li>
    <li class="contact-item item-address">
      <svg viewBox="0 0 24 24"><path d="M12 2a7 7 0 0 0-7 7c0 5 7 13 7 13s7-8 7-13a7 7 0 0 0-7-7zm0 9.5A2.5 2.5 0 1 1 12 6.5a2.5 2.5 0 0 1 0 5z"/></svg>
      <span class="contact-text">48 Tarrant St Eastwood Park,<br>Qld 4120 Australia</span>
    </li>
  </ul>
</section>

<section class="card card-back">
  <div class="coverage-map" role="img" aria-label="Map of Australia and New Zealand with Korrim location flags"></div>
  <div class="brand-name">KORRIM</div>
  <div class="badge-row">
    <div class="badge"></div>
    <div class="badge"></div>
    <div class="badge"></div>
  </div>

  <div class="range range-pallet">
    <h2 class="range-heading">Pallet containment</h2>
    <ul class="range-list"><li>Stretch</li><li>Heat shrink</li><li>Pallet hood</li></ul>
  </div>
  <div class="range range-flexible">
    <h2 class="range-heading">Flexible packaging</h2>
    <ul class="range-list"><li>Bags &amp;liners</li><li>Tube</li><li>Film &amp; sheet</li><li>Printed films (12 col)</li><li>Shrink films</li></ul>
  </div>
  <div class="range range-machinery">
    <h2 class="range-heading">Pallet wrapping<br>machinery</h2>
    <ul class="range-list"><li>Semi &amp; Fully Auto lines</li><li>Finance options include lease,Rent, Pay per wrap</li></ul>
  </div>
  <div class="range range-general">
    <h2 class="range-heading">General packaging</h2>
  </div>
</section>

</body>
</html>
```